Newsletter Design Project for electrical maintenance company

1.We need a monthly newsletter tempate designed in mail chimp.
2. We will provide the basic information for the newsletter
3. you will edit and copy write newsletter
We would love this to be an on going monthly partnership
For now, design template and do 1 newsletter
Its a light hearted news letter
40% relavent info. e.g. talk about smoke alarms
Personal information about what we are up to - family etc
update on workers - whos new, perosnal profiles etc
each newsletter to have a specific product special
e.g. $50 off second smoke alarm
Each news letter to contain 5 energy saving tips
www.brightlanehomes.com.au for more company info
Target Market(s)
residiential home owners - Mainly females
Industry/Entity Type
Electrical

```html
<!DOCTYPE html>
<html lang="en">
<head>
<meta charset="utf-8">
<title>Bright Lane Homes – Monthly Newsletter</title>
<link rel="stylesheet" href="https://fonts.googleapis.com/css2?family=Arimo:ital,wght@0,400;0,700;1,700&family=Archivo+Black&family=Noto+Serif:wght@700&display=swap">
<style>
:root{
  --black:#000;
  --orange:#f26a12;
  --orange-light:#ff9a2e;
  --white:#fff;
  --yellow:#ffe600;
  --bio-yellow:#f2e600;
  --panel:#2b2b2b;
  --red:#e8141b;
  --green:#7dc242;
  --grey-frame:#bdbdbd;
}
*{box-sizing:border-box;margin:0;padding:0}
html,body{width:924px;height:1200px;overflow:hidden;background:var(--black)}
body{font-family:Arimo,Arial,sans-serif;color:var(--white)}
.newsletter{position:relative;width:924px;height:1200px;background:var(--black);overflow:hidden}

.header-bg{position:absolute;left:0;top:0;width:924px;height:280px}
.brand-name{position:absolute;left:38px;top:38px;width:310px;font-family:"Archivo Black",Arial,sans-serif;font-size:31px;line-height:35px;color:var(--white);letter-spacing:2px}
.brand-name small{display:block;font-size:15px;line-height:18px;margin-left:140px;letter-spacing:1px}
.tagline{position:absolute;left:356px;top:38px;width:530px;font-size:19.5px;line-height:21px;color:var(--white)}
.plug-art{position:absolute;left:668px;top:118px;width:180px;height:106px;border-radius:40px 10px 10px 40px;background:radial-gradient(circle at 35% 45%,#e24a2a 0,#3a3a3a 45%,#111 100%)}
.mascot-mark{position:absolute;left:452px;top:196px;width:120px;font-family:"Archivo Black",Arial,sans-serif;font-size:13px;line-height:15px;color:var(--orange)}

.services{position:absolute;left:14px;top:268px;width:230px}
.services h2{font-family:"Noto Serif",Georgia,serif;font-size:19px;line-height:24px;color:var(--yellow);margin-bottom:5px}
.services ul{list-style:none}
.services li{font-size:16px;line-height:20.3px}
.services li::before{content:"*";font-size:12px;margin-right:6px;vertical-align:2px}
.services li.more::before{content:"";margin-right:14px}

.profile{position:absolute;left:12px;top:519px;width:212px;height:513px;background:var(--panel)}
.profile-photo{width:200px;height:270px;margin:6px;background:linear-gradient(180deg,#e9eef2 0%,#b9c3cc 55%,#2a3f8f 100%)}
.profile-bio{padding:4px 10px 0 12px;font-size:11.2px;line-height:13px;color:var(--bio-yellow)}
.profile-bio p{margin-bottom:13px}

.feature{position:absolute;left:252px;width:640px}
.feature-img{position:absolute;left:0;top:0;width:159px;border:3px solid var(--white);outline:1px solid var(--grey-frame)}
.feature-text{position:absolute;left:175px;top:-4px;width:452px;font-size:10.2px;line-height:12.4px}
.feature-text.large{font-size:12.4px;line-height:14.6px}

.offer{position:absolute;top:891px;width:125px;font-size:8px;font-weight:700}
.offer-head{height:53px;border:2px solid var(--grey-frame);background:var(--black);text-align:center;font-family:"Noto Serif",Georgia,serif;font-size:21px;line-height:20px;color:var(--red);padding-top:5px}
.offer-row{border:2px solid var(--grey-frame);border-top:none;background:var(--black)}
.offer-tag{display:inline-block;width:60px;background:var(--green);color:var(--black);font-family:"Noto Serif",Georgia,serif;font-size:8px;padding:3px 0 3px 10px}
.offer-save{font-family:"Noto Serif",Georgia,serif;color:var(--red);font-size:13px;margin-left:12px}
.offer-code{text-align:center;padding:4px 0 5px;color:var(--white);white-space:nowrap;font-size:7.6px}
.offer-label{text-align:center;padding:4px 2px 5px;color:var(--white);line-height:10px;font-size:7.6px}

.call-now{position:absolute;left:722px;top:890px;width:190px;height:112px}

.footer-bg{position:absolute;left:0;top:1053px;width:924px;height:147px;background:repeating-linear-gradient(180deg,var(--orange) 0 5px,var(--orange-light) 5px 7px)}
.footer-rule{position:absolute;left:46px;top:1060px;width:130px;height:1px;background:var(--white)}
.footer-mark{position:absolute;left:48px;top:1110px;width:140px;font-family:"Archivo Black",Arial,sans-serif;font-size:14px;line-height:17px;color:var(--black)}

.news-col{position:absolute;top:1064px;width:205px;font-size:9.6px;line-height:11.4px;color:var(--white)}
.news-col h3{font-family:"Noto Serif",Georgia,serif;font-size:11.5px;line-height:14px;margin-bottom:3px;color:var(--black)}
.energy-tips{left:200px}
.energy-tips ol{padding-left:13px}
.energy-tips li{margin-bottom:2px}
.team-news{left:418px}
.team-news p{margin-bottom:4px}

.contact{position:absolute;left:639px;top:1068px;width:280px;font-size:13.2px;line-height:15.6px}
.contact h3{font-family:"Noto Serif",Georgia,serif;font-size:14px;margin-bottom:5px}
</style>
</head>
<body>
<main class="newsletter">

  <svg class="header-bg" viewBox="0 0 924 280" aria-hidden="true">
    <defs>
      <linearGradient id="headerOrange" x1="0" y1="0" x2="0" y2="1">
        <stop offset="0" stop-color="#f26a12"/>
        <stop offset="1" stop-color="#ff9a2e"/>
      </linearGradient>
    </defs>
    <path d="M0 0H924V118C760 110 560 120 380 170C250 206 120 250 0 262Z" fill="url(#headerOrange)"/>
    <path d="M340 104C520 90 720 84 924 100" stroke="#ffffff" stroke-opacity=".25" stroke-width="1" fill="none"/>
  </svg>

  <div class="brand-name">BRIGHT LANE HOMES<small>Pty Ltd</small></div>
  <p class="tagline">Helping frustrated homeowners and small businesses in desperate need of an honest electrician who arrives on time, provides great service at a competitive price</p>
  <div class="plug-art" role="img" aria-label="Black and red electrical plug with cord"></div>
  <div class="mascot-mark">Bright Lane Homes</div>

  <section class="services">
    <h2>Electrical Services</h2>
    <ul>
      <li>Ceiling fans</li>
      <li>Lighting</li>
      <li>Smoke detectors</li>
      <li>Surge protectors</li>
      <li>Switchboard upgrades &amp;</li>
      <li>Rewires</li>
      <li>Power points</li>
      <li>Emergency repairs</li>
      <li>Fault finding</li>
      <li class="more">More..</li>
    </ul>
  </section>

  <aside class="profile">
    <div class="profile-photo" role="img" aria-label="Portrait of the founder in a blue work polo, arms crossed, in front of a white van"></div>
    <div class="profile-bio">
      <p>My name is <b><i>Daniel Marsh</i></b> licensed master electrician, founder and CEO of Bright Lane Homes.</p>
      <p>My mission at Bright Lane Homes is to provide our customers with prompt, efficient, reliable, high quality electrical repair and installation services where we are recognised as the undisputed leaders in service excellence &amp; workmanship.</p>
      <p>My aim is for each and every customer to grow and build a healthy relationship with Bright Lane Homes for life.</p>
    </div>
  </aside>

  <article class="feature" style="top:265px">
    <div class="feature-img" style="height:104px;background:linear-gradient(180deg,#fff,#e7e2d6)" role="img" aria-label="Ceiling fan with wooden blades"></div>
    <div class="feature-text">If you're looking to cool your home or office during the hot Sydney summers, install a ceiling fan. Bright Lane Homes provide an 8 point satisfaction guarantee with all services. Dedicated to reliability and affordability, you can be sure you're getting the best service in and around Sydney!<br>Enjoy the gentle breeze and cooling effect of a ceiling fan to help you sleep soundly at night and be more productive during the day. Bright Lane Homes can give you professional advice on positioning your ceiling fan to maximise its effect..</div>
  </article>

  <article class="feature" style="top:388px">
    <div class="feature-img" style="height:105px;background:radial-gradient(circle,#ffffff 20%,#d9d9d9 70%,#f4f4f4)" role="img" aria-label="White ceiling smoke alarm"></div>
    <div class="feature-text">"There is a house fire in Australia approximately every 26 minutes – is your family protected?"<br>Smoke alarms are a crucial part of any home so make sure your family has maximum protection by installing a smoke alarm at your property. Hard wired smoke alarms are installed and connected to the consumer power mains as well as having a battery backup in case of power failure, so you can feel safe knowing you're protected at all times.</div>
  </article>

  <article class="feature" style="top:510px">
    <div class="feature-img" style="height:105px;background:linear-gradient(180deg,#fff,#dde0e3)" role="img" aria-label="Grey surge protector power board"></div>
    <div class="feature-text">We invest thousands of dollars in state of the art electronic devices and insure it against theft and damage, but when it comes to protection against over voltage spikes we are unaware<br>Protect your electronic equipment such as TV's and computers. Bright Lane Homes can provide you with a first class cost effective solution that offers protection for your whole house by adding a surge arrestor at your main switchboard.<br>Lightning strikes and fluctuations in the power grid can create surge current which generates over voltage entering into your home.</div>
  </article>

  <article class="feature" style="top:634px">
    <div class="feature-img" style="height:104px;background:linear-gradient(180deg,#b9d66a,#7a6a3a 70%,#4a3a22)" role="img" aria-label="Kitchen with green walls and pendant lights"></div>
    <div class="feature-text large">Indoor lighting is the major light source provided in your home. Bright Lane Homes offer great lighting ideas and tips to help save you money and give you the light you need. Whether it's down lights, LED, ceiling lights, pendant lights or those feature chandeliers, Bright Lane Homes can help light your way.<br>Outdoor lighting can light up those dark backyards to create a more functional space. Bright Lane Homes can take care of all your exterior light installations.</div>
  </article>

  <article class="feature" style="top:756px">
    <div class="feature-img" style="height:112px;background:linear-gradient(180deg,#eef0f4,#b8bcc6)" role="img" aria-label="Row of grey electrical switchboard cabinets"></div>
    <div class="feature-text large">Upgrade your old switchboard to the latest and safest in switchboard technology to ensure maximum protection for your family.<br>Old switchboards were not designed for the heavy demand of today's consumers. Upgrade your switchboard at your Sydney home and make sure your appliances and electrical circuits are as safe as possible.Safety switches save lives. Having a safety switch installed can greatly reduce the chances of injury should an electrical fault occur. Faults can occur in appliances and in old wiring if left undetected.</div>
  </article>

  <div class="offer" style="left:252px">
    <div class="offer-head">Save<br>$50</div>
    <div class="offer-row"><span class="offer-tag">QUOTE</span><div class="offer-code">"WE850" WHEN YOU CALL</div></div>
    <div class="offer-row"><span class="offer-tag">AND</span><span class="offer-save">SAVE</span><div class="offer-label">BATHROOM LIGHT/FAN/HEAT COMBO INSTALLATIONS</div></div>
  </div>
  <div class="offer" style="left:408px">
    <div class="offer-head">Save<br>$40</div>
    <div class="offer-row"><span class="offer-tag">QUOTE</span><div class="offer-code">"CEILING40" WHEN YOU CALL</div></div>
    <div class="offer-row"><span class="offer-tag">AND</span><span class="offer-save">SAVE</span><div class="offer-label">CEILING FAN INSTALLATIONS</div></div>
  </div>
  <div class="offer" style="left:566px">
    <div class="offer-head">Save<br>$50</div>
    <div class="offer-row"><span class="offer-tag">QUOTE</span><div class="offer-code">"ALARM50" WHEN YOU CALL</div></div>
    <div class="offer-row"><span class="offer-tag">AND</span><span class="offer-save">SAVE</span><div class="offer-label">SMOKE ALARM INSTALLATIONS</div></div>
  </div>

  <svg class="call-now" viewBox="0 0 190 112" aria-label="Call now 1300 555 014">
    <path d="M8 72C6 42 50 22 110 22C150 22 172 32 178 46L184 24L182 54C186 82 140 102 80 102C36 102 10 92 8 72Z" fill="#f26a12"/>
    <g transform="rotate(-18 95 62)" font-family="'Noto Serif',Georgia,serif" font-weight="700" fill="#ffe600" text-anchor="middle">
      <text x="92" y="60" font-size="18">CALL NOW</text>
      <text x="92" y="80" font-size="15">1300 555 014</text>
    </g>
    <text x="166" y="44" font-family="'Noto Serif',Georgia,serif" font-weight="700" font-size="32" fill="#ffe600">!</text>
  </svg>

  <footer>
    <div class="footer-bg"></div>
    <div class="footer-rule"></div>
    <div class="footer-mark">Bright Lane Homes</div>

    <section class="news-col energy-tips">
      <h3>5 Energy Saving Tips</h3>
      <ol>
        <li>Swap old globes for LED down lights.</li>
        <li>Run fans before reaching for the air con.</li>
        <li>Switch appliances off at the wall at night.</li>
        <li>Wash clothes in cold water on full loads.</li>
        <li>Keep the fridge at 4°C and seals clean.</li>
      </ol>
    </section>

    <section class="news-col team-news">
      <h3>Family &amp; Team News</h3>
      <p>The Marsh family spent the school holidays camping down the south coast – the kids caught their first fish!</p>
      <p>Welcome Sam, our new apprentice. Sam loves footy, fixing old bikes and is already a whiz with smoke alarms.</p>
    </section>

    <div class="contact">
      <h3>Contact Daniel</h3>
      Phone: 1300 555 014<br>
      Email: info@brightlanehomes.com.au<br>
      Bright Lane Homes Pty Ltd<br>
      Fernhill, Sydney, Australia NSW 2199<br>
      ABN: 41 555 018 204<br>
      Lic no: 300451C
    </div>
  </footer>

</main>
</body>
</html>
```